Educational clinic needs a new webpage design

I have a relatively new website but I am unhappy with the design. I was hoping the look of it would more match my logo, brochures, business cards, and postcards. The content is good and it's already mobile ready. The designer used square space, which I would like to keep if possible. My website is www.willowgatestudio.com

Target Market(s)

Parents of school age children

Industry/Entity Type

Education

Number of Pages Required

5+ page

Requirements
Must have
• Pictures must depict the diversity of our students. We service all ages, from preschool through college and our students come from varying races.
Should not have
• I try to avoid the word "tutoring" because what we do is so much more. I like the tag line of "results that go beyond traditional tutoring"

```html
<!DOCTYPE html>
<html lang="en">
<head>
<meta charset="utf-8">
<title>Willowgate Learning Studio</title>
<link rel="stylesheet" href="https://fonts.googleapis.com/css2?family=Dosis:wght@500;600&family=Raleway:ital,wght@0,400;0,500;0,600;1,400&family=Roboto:wght@400;500;700&display=swap">
<style>
:root{
  --purple:#6a3d8f;
  --purple-dark:#5a2f7c;
  --purple-light:#9b63bf;
  --green:#8dc63f;
  --green-dark:#79b02f;
  --ink:#333;
  --muted:#666;
  --white:#fff;
  --gray:#4a4a4a;
}
*{box-sizing:border-box;margin:0;padding:0}
html,body{width:1200px;height:2799px;overflow:hidden}
body{position:relative;background:var(--white);font-family:"Raleway",sans-serif;color:var(--ink)}
.abs{position:absolute}

/* header */
.topline{left:0;top:0;width:1200px;height:4px;background:linear-gradient(90deg,var(--purple) 50%,var(--green) 50%)}
.header{left:0;top:4px;width:1200px;height:108px;background:var(--white);z-index:3}
.brand-disc{left:78px;top:22px;width:124px;height:124px;border-radius:50%;background:var(--white);z-index:2}
.brand{left:100px;top:30px;z-index:4;display:flex;align-items:center;gap:12px}
.brand-dot{width:46px;height:46px;border-radius:50%;background:var(--purple)}
.brand-name{font-family:"Roboto",sans-serif;font-weight:700;font-size:26px;line-height:1.05;color:var(--purple);letter-spacing:.5px}
.nav{top:46px;z-index:4;font-family:"Roboto",sans-serif;font-size:15px;color:var(--ink)}
.nav.active{color:var(--green);font-weight:500}
.nav-mark{left:641px;top:18px;z-index:4;width:18px;height:18px;border-radius:50%;background:var(--purple)}
.nav-under{left:640px;top:72px;z-index:4}

/* hero */
.hero{left:0;top:112px;width:1200px;height:510px;background:linear-gradient(160deg,#7a4fa0 0%,#6a3d8f 50%,#57307a 100%)}
.hero-kids{left:585px;top:150px;width:520px;height:430px;border-radius:24px;background:radial-gradient(circle at 50% 45%,#f2c04a 0%,#e2574c 35%,#4a8fd6 65%,rgba(106,61,143,0) 85%);opacity:.9}
.hero-title{left:97px;top:205px;font-family:"Roboto",sans-serif;font-weight:700;font-size:54px;color:var(--white);letter-spacing:1px}
.hero-sub{left:99px;top:292px;font-family:"Roboto",sans-serif;font-weight:500;font-size:30px;line-height:49px;color:var(--white)}
.btn{display:flex;align-items:center;justify-content:center;border-radius:8px;font-family:"Raleway",sans-serif;font-size:15px;color:var(--white)}
.hero-btn{left:99px;top:423px;width:125px;height:44px;background:var(--green);border:2px solid #a7d865}
.hero-wave{left:0;top:540px}

/* section titles */
.sec-title{left:0;width:1200px;display:flex;justify-content:center;align-items:center;gap:14px;font-family:"Dosis",sans-serif;font-weight:600;font-size:36px}
.sec-icon{width:40px;height:40px;border-radius:50%;background:var(--purple)}
.t-purple{color:var(--purple)}
.t-green{color:var(--green)}
.t-white{color:var(--white)}

/* about */
.about-title{top:690px}
.about-text{left:140px;top:774px;width:920px;text-align:center;font-size:13px;line-height:26px;color:var(--ink)}
.about-text p+p{margin-top:14px}
.about-btn{left:537px;top:916px;width:127px;height:48px;background:var(--purple);border:2px solid #8a5fb0;font-size:16px}

/* programs */
.programs{left:0;top:1008px;width:1200px;height:420px;background:var(--green)}
.dash{left:0;width:1200px;border-top:2px dashed rgba(255,255,255,.7)}
.prog-title{top:1043px}
.prog{width:340px;display:flex;align-items:center;gap:22px}
.prog-icon{flex:none;width:90px;height:90px;border-radius:50%;border:2px solid var(--white);display:flex;align-items:center;justify-content:center}
.prog-icon.fill{background:var(--purple);border-color:var(--purple)}
.prog-text{font-size:14px;line-height:25px;color:var(--white)}

/* services */
.serv-title{top:1466px}
.card{top:1567px;width:304px;height:370px;border:7px solid;border-radius:8px;background:var(--white)}
.card-photo{width:100%;height:172px}
.card-head{position:absolute;left:12px;top:188px;font-family:"Dosis",sans-serif;font-weight:600;font-size:31px}
.card-text{position:absolute;left:12px;top:238px;width:270px;font-size:13px;line-height:24px;color:var(--muted)}
.card-btn{position:absolute;left:12px;top:296px;width:98px;height:42px;font-size:14px;border:2px solid rgba(255,255,255,.4)}

/* testimonial */
.testi{left:0;top:1975px;width:1200px;height:440px;background:linear-gradient(180deg,#3d3d3d,#5a5a56 60%,#4a4a46)}
.avatar{left:527px;top:2017px;width:146px;height:146px;border-radius:50%;border:4px solid #ddd;background:radial-gradient(circle,#e8c9a6,#b98d68)}
.quote-mark{font-family:"Roboto",sans-serif;font-weight:700;font-size:72px;color:var(--white)}
.testi-text{left:130px;top:2200px;width:940px;text-align:center;font-style:italic;font-size:16px;line-height:28px;color:var(--white)}
.testi-name{left:0;top:2280px;width:1200px;text-align:center;font-size:17px;color:var(--white)}
.arrow{width:30px;height:50px}

/* footer */
.footer{left:0;top:2385px;width:1200px;height:414px;background:var(--purple)}
.foot-wave{left:0;top:2330px}
.foot-brand{left:98px;top:2520px;width:252px;text-align:center;color:var(--white)}
.foot-dot{width:56px;height:56px;border-radius:50%;background:var(--white);margin:0 auto 14px}
.foot-name{font-family:"Roboto",sans-serif;font-weight:700;font-size:22px;line-height:27px;color:var(--white)}
.foot-head{top:2440px;font-family:"Roboto",sans-serif;font-weight:500;font-size:16px;color:var(--white);padding-bottom:8px;border-bottom:2px solid var(--white)}
.links{left:416px;top:2495px;list-style:none;font-size:13px;line-height:26.7px;color:var(--white)}
.links li::before{content:"> ";}
.feat{left:621px;display:flex;gap:14px;color:var(--white)}
.feat-thumb{width:52px;height:40px}
.feat-name{font-family:"Roboto",sans-serif;font-weight:500;font-size:13px}
.feat-loc{font-size:13px;margin-top:8px;display:flex;align-items:center;gap:6px}
.contact{left:884px;display:flex;gap:20px;color:var(--white)}
.c-icon{flex:none;width:38px;height:38px;border-radius:50%;border:2px solid var(--white);display:flex;align-items:center;justify-content:center}
.c-label{font-family:"Roboto",sans-serif;font-weight:500;font-size:14px}
.c-val{font-size:12.5px;line-height:20px;margin-top:2px;width:160px}
.foot-rule{left:97px;top:2724px;width:1006px;border-top:1px solid rgba(255,255,255,.35)}
.copy{left:97px;top:2746px;font-size:13px;color:var(--white)}
.social{top:2737px;width:34px;height:34px;border-radius:50%;border:2px solid var(--white)}
</style>
</head>
<body>

<div class="abs topline"></div>
<header class="abs header"></header>
<div class="abs brand-disc"></div>
<div class="abs brand">
  <span class="brand-dot"></span>
  <span class="brand-name">Willowgate<br>Learning Studio</span>
</div>

<div class="abs nav-mark"></div>
<span class="abs nav active" style="left:632px">Home</span>
<svg class="abs nav-under" width="40" height="16" viewBox="0 0 40 16"><path d="M2 2 Q20 20 38 2" fill="none" stroke="#8dc63f" stroke-width="4" stroke-linecap="round"/></svg>
<span class="abs nav" style="left:708px">About Us</span>
<span class="abs nav" style="left:805px">Programs</span>
<span class="abs nav" style="left:907px">Who We Are</span>
<span class="abs nav" style="left:1023px">Contact Us</span>

<!-- hero -->
<section class="abs hero" role="img" aria-label="Open book photo washed in purple behind the banner"></section>
<div class="abs hero-kids" role="img" aria-label="Children sitting on large colourful letter and number blocks"></div>
<h1 class="abs hero-title">RESULTS</h1>
<p class="abs hero-sub">that Go Beyond<br>Traditional Tutoring</p>
<a class="abs btn hero-btn">Read More</a>
<svg class="abs" style="left:26px;top:345px" width="22" height="44" viewBox="0 0 22 44"><path d="M20 2 L3 22 L20 42" fill="none" stroke="#fff" stroke-width="3"/></svg>
<svg class="abs" style="left:1152px;top:345px" width="22" height="44" viewBox="0 0 22 44"><path d="M2 2 L19 22 L2 42" fill="none" stroke="#fff" stroke-width="3"/></svg>
<svg class="abs hero-wave" width="1200" height="90" viewBox="0 0 1200 90">
  <path d="M0 20 Q350 90 700 60 Q1000 35 1200 30 L1200 90 L0 90 Z" fill="#8dc63f"/>
  <path d="M0 28 Q350 100 700 72 Q1000 48 1200 48 L1200 90 L0 90 Z" fill="#fff"/>
</svg>

<!-- about -->
<h2 class="abs sec-title about-title"><span class="sec-icon"></span><span><span class="t-purple">About</span> <span class="t-green">Willowgate Learning Studio</span></span></h2>
<div class="abs about-text">
  <p>This is the place for your 'elevator pitch.' If you only had a few seconds to pitch your products or services to someone, what would you say?</p>
  <p>Willowgate Learning Studio has been helping families with their educational needs for more than 10 years. We are more than passionate about students' success. At Willowgate you'll find a welcoming environment, kind smiles and highly trained Learning Skills Specialists. Students will find a place where they will always be successful!</p>
</div>
<a class="abs btn about-btn">Read More</a>

<!-- programs -->
<section class="abs programs"></section>
<div class="abs dash" style="top:1012px"></div>
<div class="abs dash" style="top:1422px"></div>
<h2 class="abs sec-title prog-title t-white"><span class="sec-icon" style="background:#fff"></span><span>Our Programs</span></h2>

<div class="abs prog" style="left:99px;top:1144px">
  <div class="prog-icon fill"><svg width="48" height="48" viewBox="0 0 48 48" stroke="#fff" stroke-width="4" stroke-linecap="round"><path d="M6 12h14M13 5v14M28 12h14M7 31l12 12M19 31L7 43M28 37h14"/><circle cx="35" cy="30" r="1.5" fill="#fff"/><circle cx="35" cy="44" r="1.5" fill="#fff"/></svg></div>
  <p class="prog-text">Math Tutoring, both elementary, high school &amp; college</p>
</div>
<div class="abs prog" style="left:457px;top:1144px">
  <div class="prog-icon"><svg width="44" height="44" viewBox="0 0 44 44" fill="none" stroke="#fff" stroke-width="2"><path d="M4 40h36M8 40V20h28v20M4 20L22 6l18 14M18 40V30h8v10M12 25h4M28 25h4"/></svg></div>
  <p class="prog-text">ACT/SAT Prep; High School Entrance Exam Prep; GRE Prep; GED prep and more</p>
</div>
<div class="abs prog" style="left:798px;top:1144px">
  <div class="prog-icon"><svg width="40" height="44" viewBox="0 0 40 44" fill="none" stroke="#fff" stroke-width="2"><path d="M8 4h24v32H8zM8 36v4h24M12 4v32"/></svg></div>
  <p class="prog-text">The Harbor Reading Program For students who have decoding issues</p>
</div>
<div class="abs prog" style="left:99px;top:1287px">
  <div class="prog-icon"><svg width="44" height="44" viewBox="0 0 44 44" fill="none" stroke="#fff" stroke-width="2"><path d="M6 16l20-8 12 10-20 8zM6 16v8l12 10 20-8v-8M6 24v8l12 10 20-8"/></svg></div>
  <p class="prog-text">Open Reading- can be used as enrichment and for students having difficulty learning</p>
</div>
<div class="abs prog" style="left:457px;top:1287px">
  <div class="prog-icon"><svg width="40" height="44" viewBox="0 0 40 44" fill="none" stroke="#fff" stroke-width="2"><path d="M8 6h24v34H8zM14 2h12v8H14zM13 18h3M20 18h8M13 26h3M20 26h8M13 34h3M20 34h8"/></svg></div>
  <p class="prog-text">Lindgren Listening Lab- For students who read for words and not for meaning</p>
</div>
<div class="abs prog" style="left:798px;top:1287px">
  <div class="prog-icon"><svg width="44" height="44" viewBox="0 0 44 44" fill="none" stroke="#fff" stroke-width="2"><path d="M8 12h10v28H8zM18 8h10v32H18zM28 14l8-2 4 26-8 2zM11 18h4M21 14h4"/></svg></div>
  <p class="prog-text">Picture/Phrase (P/P)-For students who read well</p>
</div>

<!-- services -->
<h2 class="abs sec-title serv-title"><span class="sec-icon"></span><span><span class="t-purple">Our Center</span> <span class="t-green">Services</span></span></h2>

<article class="abs card" style="left:99px;border-color:var(--purple)">
  <div class="card-photo" role="img" aria-label="Group of smiling young students in a classroom" style="background:linear-gradient(135deg,#d9b08c,#8f6a8f)"></div>
  <h3 class="card-head" style="color:var(--purple-dark)">How to get started?</h3>
  <p class="card-text">University courses in the fields of business and management are among</p>
  <a class="card-btn btn" style="background:var(--purple)">Read More</a>
</article>
<article class="abs card" style="left:448px;border-color:var(--green)">
  <div class="card-photo" role="img" aria-label="Teenage students sitting in a row at a study table" style="background:linear-gradient(135deg,#c9a88a,#6f7f9a)"></div>
  <h3 class="card-head t-green">Who are we?</h3>
  <p class="card-text">University courses in the fields of business and management are among</p>
  <a class="card-btn btn" style="background:var(--green)">Read More</a>
</article>
<article class="abs card" style="left:797px;border-color:var(--purple-light)">
  <div class="card-photo" role="img" aria-label="Two students reading a book together" style="background:linear-gradient(135deg,#7fa0c8,#c9a0b8)"></div>
  <h3 class="card-head" style="color:var(--purple-light)">Who can we help?</h3>
  <p class="card-text">University courses in the fields of business and management are among</p>
  <a class="card-btn btn" style="background:var(--purple-light)">Read More</a>
</article>

<!-- testimonial -->
<section class="abs testi" role="img" aria-label="Dimmed photo of a student studying at a laptop"></section>
<div class="abs avatar" role="img" aria-label="Portrait of the parent giving the testimonial"></div>
<span class="abs quote-mark" style="left:432px;top:2020px">&ldquo;</span>
<span class="abs quote-mark" style="left:716px;top:2083px">&rdquo;</span>
<p class="abs testi-text">Nemo enim ipsam voluptatem quia voluptas sit aspernatur aut odit aut fugit, sed quia consequuntur magni dolores eos qui ratione voluptatem sequi nesciunt.</p>
<p class="abs testi-name">- Marisol</p>
<svg class="abs arrow" style="left:44px;top:2132px" viewBox="0 0 30 50"><path d="M25 4 L6 25 L25 46" fill="none" stroke="#fff" stroke-width="3"/></svg>
<svg class="abs arrow" style="left:1126px;top:2132px" viewBox="0 0 30 50"><path d="M5 4 L24 25 L5 46" fill="none" stroke="#fff" stroke-width="3"/></svg>

<!-- footer -->
<footer class="abs footer"></footer>
<svg class="abs foot-wave" width="1200" height="80" viewBox="0 0 1200 80">
  <path d="M0 80 L0 50 Q300 10 620 30 Q950 55 1200 20 L1200 80 Z" fill="#8dc63f"/>
  <path d="M0 80 L0 56 Q300 22 620 44 Q950 68 1200 36 L1200 80 Z" fill="#fff"/>
  <path d="M0 80 L0 66 Q300 34 620 56 Q950 78 1200 46 L1200 80 Z" fill="#6a3d8f"/>
</svg>

<div class="abs foot-brand">
  <div class="foot-dot"></div>
  <div class="foot-name">Willowgate<br>Learning Studio</div>
</div>

<h4 class="abs foot-head" style="left:416px">USEFULL LINKS</h4>
<ul class="abs links">
  <li>Home</li><li>About Us</li><li>Programs</li><li>Who we are</li><li>Learning Center</li><li>Services</li><li>Contact us</li>
</ul>

<h4 class="abs foot-head" style="left:621px">FEATURED SERVICES</h4>
<div class="abs feat" style="top:2495px"><div class="feat-thumb" role="img" aria-label="Students at home" style="background:linear-gradient(135deg,#d9a0b0,#7a4f8f)"></div><div><div class="feat-name">HOME LEARN</div><div class="feat-loc"><svg width="10" height="13" viewBox="0 0 10 13"><path d="M5 12C1 7 1 5 1 5a4 4 0 018 0s0 2-4 7z" fill="#fff"/></svg>Riverside</div></div></div>
<div class="abs feat" style="top:2555px"><div class="feat-thumb" role="img" aria-label="Students in class" style="background:linear-gradient(135deg,#9fc3d9,#c97a8f)"></div><div><div class="feat-name">STUDENTS</div><div class="feat-loc"><svg width="10" height="13" viewBox="0 0 10 13"><path d="M5 12C1 7 1 5 1 5a4 4 0 018 0s0 2-4 7z" fill="#fff"/></svg>Riverside</div></div></div>
<div class="abs feat" style="top:2615px"><div class="feat-thumb" role="img" aria-label="High school students" style="background:linear-gradient(135deg,#e0b060,#9a6fb0)"></div><div><div class="feat-name">HIGH SCHOOLS</div><div class="feat-loc"><svg width="10" height="13" viewBox="0 0 10 13"><path d="M5 12C1 7 1 5 1 5a4 4 0 018 0s0 2-4 7z" fill="#fff"/></svg>Riverside</div></div></div>

<h4 class="abs foot-head" style="left:886px">CONTACT US</h4>
<div class="abs contact" style="top:2494px"><span class="c-icon"><svg width="12" height="16" viewBox="0 0 12 16"><path d="M6 15C1 9 1 6 1 6a5 5 0 0110 0s0 3-5 9z" fill="none" stroke="#fff" stroke-width="1.6"/><circle cx="6" cy="6" r="1.6" fill="#fff"/></svg></span><div><div class="c-label">Address</div><div class="c-val">1820 Harlow Ave, Brookfield, IL 60513</div></div></div>
<div class="abs contact" style="top:2576px"><span class="c-icon"><svg width="10" height="16" viewBox="0 0 10 16"><rect x="1" y="1" width="8" height="14" rx="1.5" fill="none" stroke="#fff" stroke-width="1.6"/></svg></span><div><div class="c-label">PHONE:</div><div class="c-val">555-014-2291</div></div></div>
<div class="abs contact" style="top:2638px"><span class="c-icon"><svg width="16" height="12" viewBox="0 0 16 12"><rect x="1" y="1" width="14" height="10" rx="1" fill="#fff"/><path d="M1 1l7 6 7-6" fill="none" stroke="#6a3d8f" stroke-width="1.4"/></svg></span><div><div class="c-label">EMAIL:</div><div class="c-val">info@willowgatestudio.com</div></div></div>

<div class="abs foot-rule"></div>
<p class="abs copy">&copy; 2016 Willowgate Learning Studio. All Rights Reserved.</p>
<span class="abs social" style="left:950px"></span>
<span class="abs social" style="left:989px"></span>
<span class="abs social" style="left:1028px"></span>
<span class="abs social" style="left:1067px"></span>

</body>
</html>
```